Business Cards for Harbourline Coatings Pty Ltd

Hi every one i need a design for my buisness cards. I Want my logo in it and the name of the company needs to stand out Harbourline Coatings Pty Ltd. I want the background of the buisness cards black and i want the font to stand out in either a white or a silver stylish text. I want the design to be simple but original not to in your face if you know what i mean. I want on the back of the buisness cards to have the services that my buisness offers.
• Interior/Exterior
• Residential/Commercial
• Special effects/Texture Coatings
• Water Damage Repair
• Fully qualified
• Pensioner Discount
• 10 Year guarantee
• Fully Insured
• Obligation free quotes
full internal repaints include a proffesionla cleaning service
I want the services on the back to be layed out in an originall way not just dot points. If possible could my logo take up the whole back ground of the back but the text with the services be kind of like transparent so u cvan still see the logo i dont know if its possible it woiuld just look cool if possible. When i pick a design ill give my contact details to the designer to add to the design at the end. Any questions please just ask! Ill upload my logo.
Conatcs will include office phone: Mobile: E-mail - dale@harbourlinecoatings.com.au, Ill also have a Postal address which is a PO Box and my website is www.harbourlinecoatings.com.au

```html
<!DOCTYPE html>
<html lang="en">
<head>
<meta charset="utf-8">
<title>Harbourline Coatings Pty Ltd – Business Card</title>
<link rel="stylesheet" href="https://fonts.googleapis.com/css2?family=Arimo:wght@400;700&family=Tinos&display=swap">
<style>
  :root {
    --page: #ffffff;
    --card-front: #000000;
    --card-back: #141414;
    --ink: #ffffff;
    --soft-ink: #e6e6e6;
    --accent: #8cc63f;
    --label: #1a1a1a;
  }
  * { margin: 0; padding: 0; box-sizing: border-box; }
  html, body { width: 1200px; height: 831px; overflow: hidden; background: var(--page); }
  body { position: relative; font-family: "Arimo", Arial, sans-serif; color: var(--ink); }

  .side-label {
    position: absolute;
    font-family: "Tinos", "Times New Roman", serif;
    font-size: 34px;
    letter-spacing: 2px;
    color: var(--label);
    transform: rotate(-90deg);
    transform-origin: left top;
    white-space: nowrap;
  }
  .side-label--front { left: 86px; top: 780px; }
  .side-label--back { left: 608px; top: 780px; }

  .card {
    position: absolute;
    top: 33px;
    height: 754px;
    text-align: center;
  }
  .card--front { left: 138px; width: 462px; background: var(--card-front); }
  .card--back { left: 656px; width: 464px; background: var(--card-back); }

  .brand-mark {
    position: absolute;
    left: 168px; top: 94px;
    width: 128px; height: 128px;
    background: var(--accent);
    border-radius: 6px;
  }
  .brand-name {
    position: absolute;
    left: 0; right: 0; top: 244px;
    font-weight: 700;
    font-size: 30px;
    line-height: 36px;
    letter-spacing: 0.5px;
    color: var(--soft-ink);
  }

  .holder-name {
    position: absolute; left: 0; right: 0; top: 550px;
    font-size: 28px; font-weight: 700; color: var(--accent);
  }
  .contact-list { position: absolute; left: 0; right: 0; top: 602px; list-style: none; }
  .contact-item {
    display: flex; align-items: center; justify-content: center; gap: 8px;
    color: var(--ink);
  }
  .contact-item--office { font-size: 27px; font-weight: 700; height: 36px; }
  .contact-item--mobile { font-size: 25px; height: 34px; }
  .contact-item--email { font-size: 18px; height: 34px; }
  .contact-icon { fill: var(--ink); flex: none; }

  .services {
    position: absolute; left: 20px; right: 20px; top: 90px;
    list-style: none;
    font-size: 22px;
    line-height: 32.6px;
  }
  .service--strong { font-weight: 700; }

  .company-block { position: absolute; left: 0; right: 0; top: 608px; }
  .company-name { font-size: 18px; font-weight: 700; line-height: 26px; }
  .company-address { font-size: 16px; line-height: 24px; }
  .company-web {
    position: absolute; left: 0; right: 0; top: 676px;
    font-size: 22px; font-weight: 700; color: var(--accent);
  }
</style>
</head>
<body>
  <div class="side-label side-label--front">FRONT</div>
  <div class="side-label side-label--back">BACK</div>

  <section class="card card--front">
    <div class="brand-mark"></div>
    <div class="brand-name">HARBOURLINE COATINGS<br>PTY LTD</div>

    <div class="holder-name">Dale Morrow</div>
    <ul class="contact-list">
      <li class="contact-item contact-item--office">
        <svg class="contact-icon" width="16" height="20" viewBox="0 0 16 20" aria-hidden="true">
          <path d="M4 1 L7 5 L5 8 Q6 12 9 14 L12 12 L15 15 L12 19 Q3 17 1 6 Z"/>
        </svg>
        <span>+65 61230487</span>
      </li>
      <li class="contact-item contact-item--mobile">
        <svg class="contact-icon" width="12" height="22" viewBox="0 0 12 22" aria-hidden="true">
          <path d="M2 1 H10 Q11 1 11 2 V20 Q11 21 10 21 H2 Q1 21 1 20 V2 Q1 1 2 1 Z M3 4 V15 H9 V4 Z"/>
        </svg>
        <span>+65 89340216</span>
      </li>
      <li class="contact-item contact-item--email">
        <svg width="18" height="13" viewBox="0 0 18 13" aria-hidden="true">
          <rect x="0.75" y="0.75" width="16.5" height="11.5" fill="none" stroke="#ffffff" stroke-width="1.5"/>
          <path d="M1 1 L9 7 L17 1" fill="none" stroke="#ffffff" stroke-width="1.5"/>
        </svg>
        <span>dale@harbourlinecoatings.com.au</span>
      </li>
    </ul>
  </section>

  <section class="card card--back">
    <ul class="services">
      <li class="service">Interior/Exterior</li>
      <li class="service service--strong">Residential/Commercial</li>
      <li class="service">Special efforts/Texture coatings</li>
      <li class="service service--strong">Water damage repair</li>
      <li class="service">Fully qualified</li>
      <li class="service service--strong">Pensioner Discount</li>
      <li class="service">10 Year gurantee</li>
      <li class="service service--strong">Fully insured</li>
      <li class="service">Obligation free quotes</li>
      <li class="service service--strong">Full internal repaints inculde a<br>proffesional cleaning services</li>
    </ul>

    <div class="company-block">
      <div class="company-name">HARBOURLINE COATINGS PTY LTD</div>
      <div class="company-address">420 Linden Ave., Fairmont, CA 93100</div>
    </div>
    <div class="company-web">www.harbourlinecoatings.com.au</div>
  </section>
</body>
</html>
```